Cork Meadow Excursions Post Card/Flyer

Postcard/flyer needs to convey our mission: to provide an authentic, boutique wine tour of exceptional quality with first class customer service. It needs to be clean and high quality. Less is more :) Worthy of 5 star hotel concierges handing them to a guest. I provided an old flyer my friend made and my competitors flyer. Please use these just as reference, but i want to see your creativity. I like the format of "Gentle Harvest" -scan 91-flyer BUT I don't want to copy.

Target Market(s)

Couples, travelers, hotel employees, local industry, etc...

Industry/Entity Type

Boutique

Requirements
Must have
• Must have bullet points of the my previous reference flyer and any photos .Please use website for reference too.
• Yelp, trip advisor affirmations Plus Instagram
• "Group and Private Tours available"
• "Mention this card for 10% off any tour" - low key please
• corkmeadowexcursions.com, info@corkmeadowexcursions.com, 805-219-6384
Nice to have
• clean lines , simple and elegant
• double sided please
Should not have
• Not too busy.

```html
<!DOCTYPE html>
<html lang="en">
<head>
<meta charset="utf-8">
<title>Cork Meadow Excursions – Flyer</title>
<link rel="stylesheet" href="https://fonts.googleapis.com/css2?family=Alegreya+SC:wght@700;800&family=Cinzel:wght@500&family=Open+Sans:ital,wght@0,700;1,400&display=swap">
<style>
  :root {
    --paper-light: #eadcae;
    --paper-mid: #dcc690;
    --paper-edge: #b48a4c;
    --vine-green: #1f5220;
    --bark-brown: #6a3a1c;
    --ink-dark: #2c2416;
    --photo-frame: #2e5a2a;
    --page-bg: #f4efe4;
  }
  * { box-sizing: border-box; margin: 0; padding: 0; }
  html, body { width: 1200px; height: 960px; overflow: hidden; background: var(--page-bg); }
  .sheet { position: relative; width: 1200px; height: 960px; }
  .panel {
    position: absolute; top: 6px; width: 588px; height: 948px;
    border-radius: 14px;
    background: radial-gradient(ellipse at 50% 40%, var(--paper-light) 0%, var(--paper-mid) 70%, var(--paper-edge) 100%);
    overflow: hidden;
  }
  .panel--back { left: 6px; }
  .panel--front { left: 606px; }
  .brand {
    position: absolute; left: 0; right: 0; text-align: center;
    font-family: 'Cinzel', serif; font-weight: 500; color: var(--bark-brown);
    font-size: 27px; letter-spacing: 1px;
  }
  .brand__dot {
    display: block; width: 46px; height: 46px; margin: 0 auto 12px;
    border-radius: 50%; background: var(--vine-green);
  }
  .panel--back .brand { top: 56px; }
  .panel--front .brand { top: 90px; }
  .headline {
    position: absolute; top: 190px; left: 0; right: 0; text-align: center;
    font-family: 'Alegreya SC', serif; font-weight: 800; color: var(--bark-brown);
    font-size: 23px; letter-spacing: -0.4px;
  }
  .features {
    position: absolute; top: 254px; left: 0; right: 0; list-style: none; text-align: center;
    font-family: 'Alegreya SC', serif; font-weight: 700; color: var(--vine-green); font-size: 20px;
  }
  .features li { height: 42.5px; }
  .photo {
    position: absolute; border: 2px solid var(--photo-frame);
  }
  .photo--vehicle { left: 19px; top: 430px; width: 180px; height: 172px; background: linear-gradient(160deg, #5f8a3e, #9aa3a8 55%, #8d8570); }
  .photo--picnic { left: 204px; top: 430px; width: 180px; height: 172px; background: linear-gradient(180deg, #a9c3d6, #6f9148 40%, #c7962e 75%, #6c8b3a); }
  .photo--hillside { left: 389px; top: 430px; width: 180px; height: 172px; background: linear-gradient(180deg, #c9d6e2, #6f9a3a 35%, #8fae44); }
  .photo--guests { left: 389px; top: 608px; width: 180px; height: 172px; background: linear-gradient(180deg, #7b8c5a, #b49a7a 45%, #9a8e80 75%, #a8a39a); }
  .tours-note {
    position: absolute; left: 40px; width: 340px; top: 674px; text-align: center;
    font-family: 'Open Sans', sans-serif; font-weight: 700; color: var(--vine-green);
  }
  .tours-note__line { display: block; font-size: 21px; }
  .tours-note__emph { display: block; font-size: 26px; }
  .contact {
    position: absolute; left: 0; right: 0; text-align: center; color: var(--bark-brown);
  }
  .contact__call { top: 794px; font-family: 'Open Sans', sans-serif; font-weight: 700; font-size: 22px; }
  .contact__phone { top: 826px; font-family: 'Alegreya SC', serif; font-weight: 800; font-size: 32px; }
  .contact__web { top: 870px; font-family: 'Open Sans', sans-serif; font-style: italic; font-size: 19px; color: var(--ink-dark); }
  .contact__offer { top: 908px; font-family: 'Open Sans', sans-serif; font-style: italic; font-size: 15.5px; color: var(--ink-dark); }
  .invite {
    position: absolute; left: 0; right: 0; text-align: center;
    font-family: 'Alegreya SC', serif; font-weight: 800; color: var(--vine-green);
  }
  .invite__title { top: 230px; font-size: 68px; letter-spacing: 1px; }
  .invite__sub { top: 308px; font-size: 27px; font-weight: 700; }
  .vineyard-scene {
    position: absolute; left: 0; top: 386px; width: 588px; height: 562px;
    background: linear-gradient(180deg, rgba(220,198,144,0) 0%, #4f6a1c 10%, #3d5a18 40%, #5b7a22 70%, #3b5a1a 100%);
  }
</style>
</head>
<body>
<main class="sheet">
  <section class="panel panel--back">
    <div class="brand"><span class="brand__dot"></span>Cork Meadow Excursions</div>
    <h2 class="headline">AN AUTHENTIC AND BOUTIQUE WINE TOUR EXPERIENCE</h2>
    <ul class="features">
      <li>PREMIUM WINE TASTING AT BOUTIQUE WINERIES</li>
      <li>SAFE AND COMFORTABLE LUXURY VEHICLES</li>
      <li>PICNIC LUNCH IN A VINEYARD SETTING</li>
      <li>LOCAL EXPERT GUIDES</li>
    </ul>
    <div class="photo photo--vehicle" role="img" aria-label="Silver luxury SUV parked beside a vineyard"></div>
    <div class="photo photo--picnic" role="img" aria-label="Picnic table set with wine and plates in a vineyard"></div>
    <div class="photo photo--hillside" role="img" aria-label="Rows of vines climbing a green hillside"></div>
    <div class="photo photo--guests" role="img" aria-label="Group of guests on a utility vehicle in front of a winery barn"></div>
    <p class="tours-note"><span class="tours-note__line">GROUP AND PRIVATE TOURS</span><span class="tours-note__emph">AVAILABLE</span></p>
    <p class="contact contact__call">CONTACT US FOR AVAILABILITY</p>
    <p class="contact contact__phone">805-219-6384</p>
    <p class="contact contact__web">corkmeadowexcursions.com, &nbsp;info@corkmeadowexcursions.com</p>
    <p class="contact contact__offer">Mention “Valley Notes” for a 10% discount on any wine tour!</p>
  </section>

  <section class="panel panel--front">
    <div class="brand"><span class="brand__dot"></span>Cork Meadow Excursions</div>
    <h1 class="invite invite__title">COME EXPLORE</h1>
    <p class="invite invite__sub">SANTA BARBARA WINE COUNTRY WITH US!</p>
    <div class="vineyard-scene" role="img" aria-label="Sweeping rows of vineyard vines with a lone oak tree on the ridge"></div>
  </section>
</main>
</body>
</html>
```